Health care technology software systems

We have a solid logo. We have company colors that will need to be used as well. We just need a great business card design. We sell to health plans but want to be modern
Updates

Need extra days to review

Target Market(s)

Health technology sector selling into Health Plans

Industry/Entity Type

Health Care Technology

Contact Information for Business Card

Name, title, address, phone number, email

Requirements
Must have
• Use of Kembrata corporate colors - Uploaded w/ our logos

```html
<!DOCTYPE html>
<html lang="en">
<head>
<meta charset="utf-8">
<title>Kembrata — Business Card</title>
<link href="https://fonts.googleapis.com/css2?family=Montserrat:wght@300;400;600&display=swap" rel="stylesheet">
<style>
  :root {
    --stage: #3a3b3d;
    --card: #1e1f20;
    --white: #f4f5f6;
    --accent-blue: #0fa3e0;
    --icon-blue: #1b8fd0;
    --emboss: #2c2d2f;
  }
  * { margin: 0; padding: 0; box-sizing: border-box; }
  html, body {
    width: 1200px;
    height: 900px;
    overflow: hidden;
    background: var(--stage);
    font-family: "Montserrat", sans-serif;
  }
  .stage {
    width: 1200px;
    height: 900px;
    display: flex;
    flex-direction: column;
    align-items: center;
    justify-content: center;
    gap: 30px;
  }
  .card {
    position: relative;
    width: 700px;
    height: 400px;
    flex: none;
    background: var(--card);
    border-radius: 18px;
    box-shadow: 0 14px 30px rgba(0,0,0,0.45);
  }

  /* Front */
  .brand {
    position: absolute;
    left: 58px;
    top: 160px;
    display: flex;
    align-items: center;
    gap: 15px;
  }
  .brand-dot {
    width: 38px;
    height: 38px;
    border-radius: 50%;
    background: var(--accent-blue);
  }
  .brand-name {
    font-weight: 300;
    font-size: 54px;
    letter-spacing: 0.5px;
    color: var(--white);
    line-height: 1;
  }
  .divider {
    position: absolute;
    left: 408px;
    top: 118px;
    width: 1px;
    height: 176px;
    background: var(--accent-blue);
  }
  .contact {
    position: absolute;
    left: 436px;
    top: 117px;
    color: var(--white);
  }
  .person-name {
    font-weight: 600;
    font-size: 19px;
    letter-spacing: 0.8px;
    text-transform: uppercase;
    color: var(--accent-blue);
    line-height: 1.2;
  }
  .person-title {
    font-weight: 400;
    font-size: 15.5px;
    letter-spacing: 1px;
    text-transform: uppercase;
    margin-bottom: 7px;
    line-height: 1.3;
  }
  .address, .detail {
    font-weight: 400;
    font-size: 14.5px;
    letter-spacing: 0.7px;
    line-height: 1.45;
  }
  .details { list-style: none; margin-top: 3px; }
  .detail {
    display: flex;
    align-items: center;
    gap: 8px;
  }
  .detail svg {
    width: 12px;
    height: 12px;
    flex: none;
    fill: none;
    stroke: var(--icon-blue);
    stroke-width: 1.8;
  }

  /* Back */
  .card-back {
    display: flex;
    align-items: center;
    justify-content: center;
  }
  .back-mark {
    display: flex;
    align-items: center;
    gap: 22px;
  }
  .back-circle {
    width: 86px;
    height: 86px;
    border-radius: 50%;
    background: var(--emboss);
  }
  .back-name {
    font-weight: 300;
    font-size: 64px;
    line-height: 1;
    color: var(--emboss);
  }
</style>
</head>
<body>
<main class="stage">
  <article class="card card-front">
    <div class="brand">
      <span class="brand-dot"></span>
      <span class="brand-name">kembrata</span>
    </div>

    <span class="divider"></span>

    <section class="contact">
      <h1 class="person-name">Daniel Reyes</h1>
      <p class="person-title">Director</p>
      <p class="address">2718 Alder Lane<br>Brookfield, CO 80520</p>
      <ul class="details">
        <li class="detail">
          <svg viewBox="0 0 16 16" aria-hidden="true"><path d="M4 1.5l2.5 3-1.5 1.5c.8 1.8 2.2 3.2 4 4l1.5-1.5 3 2.5-1.5 2.5C7 13.5 2.5 9 1.5 3z"/></svg>
          +330 5128-4470
        </li>
        <li class="detail">
          <svg viewBox="0 0 16 16" aria-hidden="true"><rect x="1.5" y="3.5" width="13" height="9" rx="1"/><path d="M1.5 4l6.5 5 6.5-5"/></svg>
          info@kembrata.com
        </li>
        <li class="detail">
          <svg viewBox="0 0 16 16" aria-hidden="true"><circle cx="8" cy="8" r="6.5"/><path d="M1.5 8h13M8 1.5c-3 3.5-3 9.5 0 13M8 1.5c3 3.5 3 9.5 0 13"/></svg>
          www.kembrata.com
        </li>
      </ul>
    </section>
  </article>

  <article class="card card-back">
    <div class="back-mark">
      <span class="back-circle"></span>
      <span class="back-name">kembrata</span>
    </div>
  </article>
</main>
</body>
</html>
```